Unique Private Wine Label for Wine Bottles (UPDATED BRIEF)

Updated Brief Oct 15, 2017. Please see below!

I am looking for a unique wine label designs for my wine bottles. I create wine and would like to have wine labels for my bottles. I am looking for a main label and then several additional labels with the same design just with the type of wine listed on the label (see below for wine types). This is private wine for family and friends to consume not commercially produced wine.

I would like a rustic, classic or vintage design with some color in the label. I do have a specific name for the wine which i like to call "Fernhollow" . I would like to see different designs.

We would like vintage or classic labels. Please give me a few multiple designs based on above. I also want to have a main label and then incorporate different types of wine into the labels like "Chardonnay" or "Pinot Noir" or "Sauvignon Blanc" or "Caberent Savignon" or "Merlot" below the name of the wine. As an example, the labels will be the same design but the word Sauvignon Blanc will be incorporated into the design for this type of wine label and so on for the other types of wine.

Please let me know if you have any questions.

Reason: I Have changed the vision of the design. I would like a classic, rustic or vintage design NOT a beach theme. The brief has been updated as of Oct 15, 2017. Please see updated brief for instructions on new design

Note: I have changed the vision of the design. I would like a classic, rustic or vintage design NOT a beach theme. The brief has been updated as of Oct 15, 2017. Please see updated brief for instructions on new design. I would like new designers to provide new designs! Payment is Guaranteed! Thanks!

Target Market(s)

This is private wine for family and friends to consume not commercially produced wine.

Font styles to use
Decorative
Script

Colors

Designer to choose colors to be used in the design.

Requirements
Must have
• Updated Brief Oct 15, 2017. Please see below!
• I am looking for a unique wine label designs for my wine bottles. I create wine and would like to have wine labels for my bottles. I am looking for a main label and then several additional labels with the same design just with the type of wine listed on the label (see below for wine types). This is private wine for family and friends to consume not commercially produced wine.
• I would like a rustic, classic or vintage design with some color in the label. I do have a specific name for the wine which i like to call "Fernhollow". I would like to see different designs.
• We would like vintage or classic labels. Please give me a few multiple designs based on above. I also want to have a main label and then incorporate different types of wine into the labels like "Chardonnay" or "Pinot Noir" or "Sauvignon Blanc" or "Caberent Savignon" or "Merlot" below the name of the wine. As an example, the labels will be the same design but the word Sauvignon Blanc will be incorporated into the design for this type of wine label and so on for the other types of wine.
• Please let me know if you have any questions.
Nice to have
Should not have
• Please see the updated brief instructions above. I DO NOT WANT A BEACH THEME ANYMORE!

```html
<!DOCTYPE html>
<html lang="en">
<head>
<meta charset="utf-8">
<title>Fernhollow Vineyards – Wine Label</title>
<link rel="stylesheet" href="https://fonts.googleapis.com/css2?family=Libre+Caslon+Text:ital@0;1&display=swap">
<style>
  :root {
    --page-bg: #efede8;
    --label-top: #e6df62;
    --label-mid: #bcd79c;
    --label-bottom: #74b8bd;
    --ink: #2a3147;
    --rule: #3b4658;
    --frame: #fbf8ef;
    --scene-light: #f3f5f4;
    --scene-sky: #d3e1e6;
    --scene-sea: #97b6c8;
    --ring: #3a93ad;
  }
  html, body {
    margin: 0;
    padding: 0;
    width: 698px;
    height: 1200px;
    overflow: hidden;
    background: var(--page-bg);
  }
  .wine-label {
    position: absolute;
    left: 39px;
    top: 26px;
    width: 620px;
    height: 1150px;
    display: block;
  }
  .label-type {
    font-family: "Libre Caslon Text", Georgia, serif;
    font-variant-numeric: lining-nums;
    fill: var(--ink);
  }
  .label-copy {
    font-family: "Libre Caslon Text", Georgia, serif;
    font-style: italic;
    fill: var(--ink);
  }
</style>
</head>
<body>
<svg class="wine-label" viewBox="0 0 620 1150" xmlns="http://www.w3.org/2000/svg">
  <defs>
    <linearGradient id="label-fill" x1="0" y1="0" x2="0" y2="1">
      <stop offset="0" stop-color="var(--label-top)"/>
      <stop offset="0.45" stop-color="var(--label-mid)"/>
      <stop offset="1" stop-color="var(--label-bottom)"/>
    </linearGradient>
    <radialGradient id="scene-fill" cx="0.5" cy="0.45" r="0.6">
      <stop offset="0" stop-color="var(--scene-light)"/>
      <stop offset="0.7" stop-color="var(--scene-sky)"/>
      <stop offset="1" stop-color="var(--scene-sea)"/>
    </radialGradient>
    <path id="name-arc" d="M50,345 Q310,165 570,345"/>
  </defs>

  <path class="label-shape" fill="url(#label-fill)"
        d="M0,110 C25,110 40,95 40,70 Q310,-10 580,70 C580,95 595,110 620,110 L620,1150 L0,1150 Z"/>
  <path class="label-frame" fill="none" stroke="var(--frame)" stroke-width="3"
        d="M14,124 C40,124 54,108 54,84 Q310,8 566,84 C566,108 580,124 606,124 L606,1095 L14,1095 Z"/>

  <text class="label-type" font-size="60">
    <textPath href="#name-arc" startOffset="50%" text-anchor="middle" textLength="470" lengthAdjust="spacing">FERNHOLLOW</textPath>
  </text>

  <circle cx="310" cy="290" r="8" fill="none" stroke="var(--frame)" stroke-width="4"/>

  <ellipse cx="310" cy="465" rx="220" ry="142" fill="none" stroke="var(--ring)" stroke-width="4"/>
  <ellipse class="label-vignette" cx="310" cy="465" rx="210" ry="132" fill="url(#scene-fill)"
           role="img" aria-label="Sketched seaside scene with palm trees and a setting sun"/>

  <text class="label-type" x="310" y="762" font-size="78" text-anchor="middle" textLength="500" lengthAdjust="spacingAndGlyphs">VINEYARDS</text>
  <line x1="70" y1="836" x2="550" y2="836" stroke="var(--rule)" stroke-width="2"/>

  <text class="label-copy" x="310" y="888" font-size="20" text-anchor="middle" textLength="500" lengthAdjust="spacingAndGlyphs">Hand crafted in small batches from our family vineyard,</text>
  <text class="label-copy" x="310" y="926" font-size="20" text-anchor="middle" textLength="520" lengthAdjust="spacingAndGlyphs">aged slowly in oak and shared with the people we love most.</text>

  <text class="label-type" x="310" y="1052" font-size="30" text-anchor="middle">750ML</text>

  <line x1="0" y1="1112" x2="620" y2="1112" stroke="var(--frame)" stroke-width="4"/>
  <line x1="0" y1="1128" x2="620" y2="1128" stroke="var(--frame)" stroke-width="2"/>
</svg>
</body>
</html>
```